BRL business card

For a business card with our logo

Contact Information for Business Card

Mathéo VRANEL
Founder & CEO
email : ceo@brightlanterncollective.com / www.brightlanterncollective.com /
instagram / facebook / WhatsApp
N°: +590 690 482 517

Colors

Designer to choose colors to be used in the design.

```html
<!DOCTYPE html>
<html lang="en">
<head>
<meta charset="utf-8">
<title>BRL business card</title>
<link href="https://fonts.googleapis.com/css2?family=Lora:wght@400;500&display=swap" rel="stylesheet">
<style>
  :root {
    --stage: #3c3d40;
    --card-dark: #151518;
    --card-light: #ffffff;
    --brand-blue: #1a5cb0;
    --brand-orange: #f0762a;
    --ink: #1f1f1f;
    --rule: #2a2a2a;
  }
  * { margin: 0; padding: 0; box-sizing: border-box; }
  html, body {
    width: 1200px; height: 874px; overflow: hidden;
    background: var(--stage);
    font-family: "Lora", serif;
  }
  .stage { position: relative; width: 1200px; height: 874px; }

  .card {
    position: absolute;
    width: 560px; height: 320px;
    border-radius: 22px;
    overflow: hidden;
    border-bottom: 7px solid var(--brand-blue);
  }
  .card--back { left: 80px; top: 70px; background: var(--card-dark); }
  .card--front { left: 560px; top: 470px; background: var(--card-light); }

  .wordmark {
    position: absolute;
    display: flex; align-items: center; gap: 14px;
  }
  .wordmark__dot {
    width: 54px; height: 54px; border-radius: 50%;
    background: var(--brand-orange); flex: none;
  }
  .wordmark__name {
    color: var(--brand-blue);
    font-weight: 500;
    font-size: 25px;
    line-height: 1.1;
    letter-spacing: 0.5px;
    text-transform: uppercase;
    white-space: nowrap;
  }
  .wordmark__rule {
    position: absolute; left: 0; right: 0; bottom: -12px;
    height: 1.5px; background: var(--brand-orange);
  }

  .card--back .wordmark { left: 130px; top: 110px; }

  .social {
    position: absolute; left: 0; right: 0; top: 230px;
    display: flex; justify-content: center; gap: 12px;
  }
  .social__dot { width: 22px; height: 22px; border-radius: 50%; }
  .social__dot--blue { background: var(--brand-blue); }
  .social__dot--orange { background: var(--brand-orange); }

  .card--front .wordmark { left: 28px; top: 122px; gap: 12px; }
  .card--front .wordmark__name { font-size: 18px; letter-spacing: 0.3px; }
  .card--front .wordmark__dot { width: 42px; height: 42px; }

  .divider { position: absolute; left: 272px; top: 60px; }

  .contact { position: absolute; left: 300px; top: 68px; }
  .contact__name {
    color: var(--brand-blue);
    font-size: 25px; font-weight: 400;
    text-transform: uppercase; letter-spacing: 0.3px;
    white-space: nowrap;
  }
  .contact__role { color: var(--ink); font-size: 14px; margin-top: 2px; }
  .contact__list { list-style: none; margin-top: 30px; }
  .contact__item {
    display: flex; align-items: center; gap: 10px;
    font-size: 12.5px; color: var(--ink);
    margin-bottom: 9px; white-space: nowrap;
  }
  .contact__icon {
    width: 18px; height: 18px; border-radius: 50%;
    display: flex; align-items: center; justify-content: center; flex: none;
  }
  .contact__icon--phone { background: #5cb85c; }
  .contact__icon--mail, .contact__icon--web { background: var(--brand-orange); }
</style>
</head>
<body>
<main class="stage">

  <section class="card card--back" aria-label="Card back">
    <div class="wordmark">
      <span class="wordmark__dot"></span>
      <span class="wordmark__name">Bright Lantern<br>Collective</span>
      <span class="wordmark__rule"></span>
    </div>
    <div class="social" aria-label="Social profiles">
      <span class="social__dot social__dot--blue"></span>
      <span class="social__dot social__dot--orange"></span>
    </div>
  </section>

  <section class="card card--front" aria-label="Card front">
    <div class="wordmark">
      <span class="wordmark__dot"></span>
      <span class="wordmark__name">Bright Lantern<br>Collective</span>
      <span class="wordmark__rule"></span>
    </div>

    <svg class="divider" width="20" height="200" viewBox="0 0 20 200" aria-hidden="true">
      <line x1="0" y1="0" x2="2" y2="200" stroke="var(--rule)" stroke-width="1.2"/>
    </svg>

    <div class="contact">
      <h1 class="contact__name">Mathéo VRANEL</h1>
      <p class="contact__role">Founder &amp; CEO</p>
      <ul class="contact__list">
        <li class="contact__item">
          <span class="contact__icon contact__icon--phone">
            <svg width="10" height="10" viewBox="0 0 24 24" aria-hidden="true"><path fill="#fff" d="M6.6 10.8a15 15 0 0 0 6.6 6.6l2.2-2.2a1 1 0 0 1 1-.25 11.4 11.4 0 0 0 3.6.57 1 1 0 0 1 1 1V20a1 1 0 0 1-1 1A17 17 0 0 1 3 4a1 1 0 0 1 1-1h3.5a1 1 0 0 1 1 1c0 1.25.2 2.450.57 3.6a1 1 0 0 1-.25 1z"/></svg>
          </span>
          +590 690 482 517
        </li>
        <li class="contact__item">
          <span class="contact__icon contact__icon--mail">
            <svg width="10" height="10" viewBox="0 0 24 24" aria-hidden="true"><rect x="2" y="5" width="20" height="14" rx="1" fill="none" stroke="#fff" stroke-width="2.2"/><path d="M2 6l10 7 10-7" fill="none" stroke="#fff" stroke-width="2.2"/></svg>
          </span>
          ceo@brightlanterncollective.com
        </li>
        <li class="contact__item">
          <span class="contact__icon contact__icon--web">
            <svg width="10" height="10" viewBox="0 0 24 24" aria-hidden="true"><circle cx="12" cy="12" r="9" fill="none" stroke="#fff" stroke-width="2"/><path d="M3 12h18M12 3c3 3 3 15 0 18M12 3c-3 3-3 15 0 18" fill="none" stroke="#fff" stroke-width="1.6"/></svg>
          </span>
          www.brightlanterncollective.com
        </li>
      </ul>
    </div>
  </section>

</main>
</body>
</html>
```